Flyer Design

We are a property company and need attractive flyers that will grab peoples attention. We want them to be bold but simple and not too busy. I attach a draft and also our logo. We will print in A5 size.
Thank you & I look forward to receiving designs.

It Company

```html
<!DOCTYPE html>
<html lang="en">
<head>
<meta charset="utf-8">
<title>ORA Subdivisions Flyer</title>
<link href="https://fonts.googleapis.com/css2?family=Montserrat:wght@500;600;700;800&display=swap" rel="stylesheet">
<style>
  :root {
    --sky-top: #7f9fc8;
    --sky-mid: #b9c9de;
    --house-tone: #a89880;
    --lawn: #5d6b3e;
    --overlay: rgba(28, 28, 30, 0.72);
    --white: #ffffff;
    --ink: #111111;
    --accent-red: #b8372b;
    --charcoal: #3b3b3c;
    --footer: #1b1b1b;
  }
  * { margin: 0; padding: 0; box-sizing: border-box; }
  html, body { width: 858px; height: 1200px; overflow: hidden; background: var(--white); }
  body { font-family: "Montserrat", Arial, sans-serif; }
  .flyer { position: relative; width: 858px; height: 1200px; overflow: hidden; }

  .hero {
    position: absolute; left: 0; top: 0; width: 858px; height: 640px;
    background: linear-gradient(180deg, var(--sky-top) 0%, var(--sky-mid) 35%, var(--house-tone) 62%, var(--lawn) 100%);
  }
  .hero-band {
    position: absolute; left: 0; top: 450px; width: 858px; height: 190px;
    background: var(--overlay);
    display: flex; align-items: center; justify-content: center;
  }
  .hero-headline {
    color: var(--white); font-weight: 800; font-size: 38px; line-height: 48px;
    text-align: center; letter-spacing: 0.2px;
  }

  .offer {
    position: absolute; left: 0; top: 640px; width: 858px; height: 256px;
    background: var(--white); text-align: center;
  }
  .offer-question {
    margin-top: 60px; color: var(--accent-red); font-weight: 800;
    font-size: 28px; letter-spacing: 0.3px; text-transform: uppercase;
  }
  .offer-text {
    margin-top: 30px; color: var(--ink); font-weight: 500;
    font-size: 32px; line-height: 46px;
  }

  .contact {
    position: absolute; left: 0; top: 896px; width: 858px; height: 202px;
    background: var(--charcoal); display: flex; align-items: center; justify-content: center;
  }
  .contact-text {
    color: var(--white); font-weight: 600; font-size: 26px; line-height: 45px; text-align: center;
  }

  .footer {
    position: absolute; left: 0; top: 1098px; width: 858px; height: 102px;
    background: var(--footer); display: flex; align-items: center;
  }
  .brand-block {
    width: 203px; height: 102px; background: var(--accent-red);
    display: flex; align-items: center; justify-content: center;
  }
  .brand-name { color: var(--white); font-weight: 800; font-size: 34px; letter-spacing: 2px; }
  .web-address {
    flex: 1; text-align: center; color: var(--white); font-weight: 700;
    font-size: 35px; letter-spacing: 2.5px;
  }
</style>
</head>
<body>
  <main class="flyer">
    <section class="hero" role="img" aria-label="Photograph of a two-storey suburban house with neighbouring homes under a blue sky">
      <div class="hero-band">
        <h1 class="hero-headline">Are you a homeowner looking<br>for financial freedom while been<br>able to keep your own home?</h1>
      </div>
    </section>

    <section class="offer">
      <h2 class="offer-question">Are you struggling to pay your mortgage?</h2>
      <p class="offer-text">ORA specialise in subdivisions including<br>finance and management.</p>
    </section>

    <section class="contact">
      <p class="contact-text">Call 021 555 0147 or email info@orasubdivisions.com<br>for more information or to find out ifyour property is<br>suitable for subdivision in Auckland.</p>
    </section>

    <footer class="footer">
      <div class="brand-block"><span class="brand-name">ORA</span></div>
      <p class="web-address">www.orasubdivisions.com</p>
    </footer>
  </main>
</body>
</html>
```